Australian Recruitment Agency Flyer

We are looking for a 1 page flyer to promote our recruitment company. We would like this to have a corporate look.

Attached is a word document with the content we would like included in the flyer.

I have also attached some of our clients logos to be included in the flyer

Target Market(s)

Professional organisations looking to hire new staff

Industry/Entity Type

It Company

Colors
85abd2
3176b5
31b7a3
d2a4cc
e667a6
b768aa
876aae
3276b5
f04a50

Requirements
Must have
• Must have the content that we have include on a word document in the design brief.

```html
<!DOCTYPE html>
<html lang="en">
<head>
<meta charset="utf-8">
<title>TalentHarbor Recruitment Flyer</title>
<link href="https://fonts.googleapis.com/css2?family=Roboto:ital,wght@0,300;0,400;0,500;0,700;1,700&family=Roboto+Condensed:wght@400&display=swap" rel="stylesheet">
<style>
  :root {
    --page-bg: #e6e6e8;
    --navy-deep: #0b1020;
    --navy: #141c36;
    --brand-blue: #3176b5;
    --sky: #85abd2;
    --teal: #31b7a3;
    --pink: #e667a6;
    --violet: #876aae;
    --plum: #b768aa;
    --red: #f04a50;
    --white: #ffffff;
    --soft-white: #e9edf5;
    --strip-text: #2b2f3a;
  }
  * { box-sizing: border-box; margin: 0; padding: 0; }
  html, body { width: 1200px; height: 1200px; overflow: hidden; }
  body {
    background: var(--page-bg);
    font-family: "Roboto", Arial, sans-serif;
    position: relative;
  }
  .flyer {
    position: absolute;
    left: 152px; top: 21px;
    width: 895px; height: 1157px;
    background: linear-gradient(180deg, var(--navy-deep) 0%, var(--navy) 40%, #10152b 75%, var(--navy-deep) 100%);
    overflow: hidden;
    color: var(--white);
  }
  .hero-visual {
    position: absolute;
    left: 0; top: 200px; width: 100%; height: 640px;
    background:
      radial-gradient(ellipse 40% 35% at 12% 40%, rgba(240,74,80,.55), transparent 70%),
      radial-gradient(ellipse 30% 30% at 8% 25%, rgba(230,190,70,.45), transparent 70%),
      radial-gradient(ellipse 35% 30% at 35% 45%, rgba(230,103,166,.35), transparent 70%),
      radial-gradient(ellipse 45% 40% at 70% 35%, rgba(135,106,174,.45), transparent 70%),
      radial-gradient(ellipse 60% 40% at 50% 20%, rgba(133,171,210,.35), transparent 70%),
      radial-gradient(ellipse 70% 35% at 50% 75%, rgba(90,110,150,.55), transparent 75%),
      linear-gradient(180deg, rgba(20,28,54,0) 0%, rgba(40,55,90,.6) 55%, rgba(16,21,43,1) 100%);
  }
  .brand {
    position: absolute; top: 110px; left: 0; width: 100%;
    display: flex; justify-content: center; align-items: center; gap: 22px;
  }
  .brand-dot {
    width: 86px; height: 86px; border-radius: 50%;
    background: var(--brand-blue);
  }
  .brand-text { display: flex; flex-direction: column; align-items: center; }
  .brand-name {
    font-size: 54px; font-weight: 500; color: var(--brand-blue); line-height: 1; letter-spacing: -1px;
  }
  .brand-tag { font-size: 16px; font-weight: 400; color: var(--brand-blue); margin-top: 8px; letter-spacing: .3px; }
  .headline {
    position: absolute; top: 225px; left: 0; width: 100%;
    text-align: center; font-weight: 300; font-size: 34px; line-height: 41px;
  }
  .testimonial {
    position: absolute; top: 340px; left: 0; width: 100%; text-align: center;
    font-family: "Roboto Condensed", Arial, sans-serif; font-size: 22px; line-height: 26px;
  }
  .quote-mark { font-family: Georgia, serif; font-weight: 700; font-size: 52px; line-height: 0; vertical-align: -18px; }
  .attribution {
    position: absolute; top: 437px; left: 520px; width: 200px; text-align: center;
    font-style: italic; font-weight: 700; font-size: 11px; line-height: 14px;
  }
  .section-title { font-weight: 300; font-size: 34px; letter-spacing: .3px; line-height: 1; }
  .what-we-do { position: absolute; top: 820px; left: 64px; width: 340px; }
  .what-we-do p { margin-top: 20px; font-size: 14.5px; line-height: 17.5px; color: var(--soft-white); }
  .industries { position: absolute; top: 820px; left: 455px; width: 420px; }
  .industry-list {
    margin-top: 22px; list-style: none;
    display: grid; grid-template-columns: 183px 220px; row-gap: 8px;
    font-size: 14.5px; font-weight: 500;
  }
  .industry-list li { display: flex; align-items: center; gap: 11px; }
  .tick { width: 12px; height: 10px; flex: none; }
  .client-strip {
    position: absolute; top: 961px; left: 0; width: 100%; height: 64px;
    background: var(--white);
    display: flex; justify-content: space-around; align-items: center; padding: 0 30px;
    color: var(--strip-text); font-size: 19px; font-weight: 500;
  }
  .client { display: flex; align-items: center; gap: 6px; }
  .client-square { width: 14px; height: 14px; background: var(--brand-blue); }
  .client-circle { width: 16px; height: 16px; border-radius: 50%; background: var(--teal); }
  .cta {
    position: absolute; top: 1030px; left: 0; width: 100%; height: 80px;
    background: #05070f;
    display: flex; align-items: center; justify-content: center; text-align: center;
    font-size: 27px; font-weight: 500; line-height: 33px;
  }
  .flyer-base { position: absolute; top: 1110px; left: 0; width: 100%; height: 47px; background: #0a0a0c; }
</style>
</head>
<body>
  <main class="flyer">
    <div class="hero-visual" role="img" aria-label="Colourful triangle pattern over a world map, a team of business professionals standing behind a close-up handshake"></div>

    <header class="brand">
      <span class="brand-dot"></span>
      <div class="brand-text">
        <span class="brand-name">TalentHarbor</span>
        <span class="brand-tag">Human Resources &amp; Recruitment</span>
      </div>
    </header>

    <h1 class="headline">We have over 20 years of experience<br>helping companies hire amazing talent</h1>

    <blockquote class="testimonial">
      <span class="quote-mark">&ldquo;</span> TalentHarbor really delivered on their promise and<br>
      far exceeded our expectations.<br>
      Their fixed fee model saved us thousands <span class="quote-mark">&rdquo;</span>
    </blockquote>
    <p class="attribution">Mark Ellison General Manager<br>Harbour Financial Services</p>

    <section class="what-we-do">
      <h2 class="section-title">WHAT WE DO</h2>
      <p>We aren’t a recruitment agency, we are an extension of your team. We become your very own HR &amp; Recruitment department to be called upon as and when needed.</p>
    </section>

    <section class="industries">
      <h2 class="section-title">INDUSTRIES WE SERVE</h2>
      <ul class="industry-list">
        <li><svg class="tick" viewBox="0 0 12 10"><path d="M1 5 L4.5 8.5 L11 1" fill="none" stroke="#8c93a6" stroke-width="2"/></svg>Mining and Oil &amp; Gas</li>
        <li><svg class="tick" viewBox="0 0 12 10"><path d="M1 5 L4.5 8.5 L11 1" fill="none" stroke="#8c93a6" stroke-width="2"/></svg>IT &amp; Communications</li>
        <li><svg class="tick" viewBox="0 0 12 10"><path d="M1 5 L4.5 8.5 L11 1" fill="none" stroke="#8c93a6" stroke-width="2"/></svg>Accounting &amp; Finance</li>
        <li><svg class="tick" viewBox="0 0 12 10"><path d="M1 5 L4.5 8.5 L11 1" fill="none" stroke="#8c93a6" stroke-width="2"/></svg>Government &amp; Not for Profit</li>
        <li><svg class="tick" viewBox="0 0 12 10"><path d="M1 5 L4.5 8.5 L11 1" fill="none" stroke="#8c93a6" stroke-width="2"/></svg>Sales &amp; Marketing</li>
      </ul>
    </section>

    <div class="client-strip" aria-label="Our clients">
      <span class="client">roadline</span>
      <span class="client"><span class="client-square"></span>APEX</span>
      <span class="client">Cobalt Australia</span>
      <span class="client">Southern Metals</span>
      <span class="client">hfs</span>
      <span class="client">arden process<span class="client-circle"></span></span>
      <span class="client">NOVA</span>
    </div>

    <div class="cta">Start a conversation today and see why these<br>companies turn to us time and time again</div>
    <div class="flyer-base"></div>
  </main>
</body>
</html>
```